CloudRiver Business Card

I need something that flows with the logo and looks professional but creative. I included the thumbnail file of the photo but will upload the source file once I have it. Colors of business card should flow. I am interested in doing the translucent clear plastic cards as well. My company is called CloudRiver in one word and the contact details are below:

Dale Hollings
555-318-4720
www.CloudRiverTx.example
dhollings_47@mailbox.example
Updates

Too much red. I'd rather focus on the blue and put some silver or grey in there.

New Files uploaded. Like the designs so far and am looking forward to seeing more.

Looking for a whole new direction. Let's forget about the plastic card. Let's focus on the blue more than red. I still haven't seen something that really grabs me.

Industry/Entity Type

Plastic

```html
<!DOCTYPE html>
<html lang="en">
<head>
<meta charset="utf-8">
<title>CloudRiver Business Card</title>
<link href="https://fonts.googleapis.com/css2?family=Lato:wght@400;700&display=swap" rel="stylesheet">
<style>
  :root {
    --page-bg: #e4e2df;
    --card-top: #f3f2f0;
    --card-bottom: #e6e5e3;
    --card-edge: #6b6b6b;
    --brand-red: #c1343c;
    --icon-red: #a3232a;
    --band-navy: #1f3a66;
    --band-navy-deep: #17305a;
    --rule-red: #c42d34;
    --name-text: #e9edf4;
    --body-text: #1c1c1c;
  }
  html, body {
    margin: 0;
    padding: 0;
    width: 970px;
    height: 1200px;
    overflow: hidden;
    background: var(--page-bg);
  }
  .canvas {
    position: relative;
    width: 970px;
    height: 1200px;
  }
  .card {
    position: absolute;
    left: 185px;
    top: 60px;
    width: 600px;
    height: 1080px;
    border-radius: 24px;
    border: 1.5px solid var(--card-edge);
    background: linear-gradient(180deg, var(--card-top), var(--card-bottom));
    box-sizing: border-box;
    overflow: hidden;
    font-family: "Lato", sans-serif;
  }
  .brand-name {
    position: absolute;
    top: 140px;
    left: 0;
    width: 100%;
    text-align: center;
    font-size: 74px;
    font-weight: 400;
    line-height: 1;
    color: var(--brand-red);
    letter-spacing: -0.5px;
  }
  .name-band {
    position: absolute;
    left: 0;
    top: 326px;
    width: 100%;
    height: 112px;
  }
  .name-band .rule {
    position: absolute;
    left: 0;
    width: 100%;
    height: 5px;
    background: var(--rule-red);
  }
  .name-band .rule.top { top: 0; }
  .name-band .rule.bottom { bottom: 0; }
  .name-band .bar {
    position: absolute;
    left: 0;
    top: 14px;
    width: 100%;
    height: 84px;
    background: linear-gradient(90deg, var(--band-navy-deep), var(--band-navy));
    display: flex;
    align-items: center;
    justify-content: center;
  }
  .person-name {
    margin: 0;
    font-size: 31px;
    font-weight: 700;
    letter-spacing: 0.5px;
    color: var(--name-text);
    text-transform: uppercase;
  }
  .contact {
    position: absolute;
    left: 0;
    width: 100%;
    display: flex;
    flex-direction: column;
    align-items: center;
  }
  .contact.phone { top: 606px; }
  .contact.email { top: 729px; }
  .contact.web { top: 859px; }
  .contact svg {
    width: 42px;
    height: 42px;
    display: block;
  }
  .contact .value {
    margin-top: 12px;
    font-size: 24px;
    color: var(--body-text);
  }
</style>
</head>
<body>
<div class="canvas">
  <div class="card">
    <div class="brand-name">CloudRiver</div>

    <div class="name-band">
      <div class="rule top"></div>
      <div class="bar"><h1 class="person-name">Dale Hollings</h1></div>
      <div class="rule bottom"></div>
    </div>

    <div class="contact phone">
      <svg viewBox="0 0 42 42" aria-hidden="true">
        <circle cx="21" cy="21" r="21" fill="var(--icon-red)"/>
        <path d="M12 17c0-3 4-5 9-5s9 2 9 5v2h-5v-2h-8v2h-5z" fill="#fff"/>
        <rect x="13" y="21" width="16" height="9" rx="2" fill="#fff"/>
        <circle cx="21" cy="25.5" r="2.5" fill="var(--icon-red)"/>
      </svg>
      <div class="value">555-318-4720</div>
    </div>

    <div class="contact email">
      <svg viewBox="0 0 42 42" aria-hidden="true">
        <circle cx="21" cy="21" r="21" fill="var(--icon-red)"/>
        <rect x="11" y="14" width="20" height="14" fill="none" stroke="#fff" stroke-width="2"/>
        <path d="M11 14l10 8 10-8M11 28l7-7M31 28l-7-7" fill="none" stroke="#fff" stroke-width="2"/>
      </svg>
      <div class="value">dhollings_47@mailbox.example</div>
    </div>

    <div class="contact web">
      <svg viewBox="0 0 42 42" aria-hidden="true">
        <circle cx="21" cy="21" r="21" fill="var(--icon-red)"/>
        <g fill="none" stroke="#fff" stroke-width="1.8">
          <circle cx="21" cy="21" r="10"/>
          <ellipse cx="21" cy="21" rx="4.5" ry="10"/>
          <path d="M11 21h20M13 15.5h16M13 26.5h16"/>
        </g>
      </svg>
      <div class="value">www.CloudRiverTx.example</div>
    </div>
  </div>
</div>
</body>
</html>
```